Stylish Business Cards Wanted

- DOUBLE SIDED Design Required -

High end, edgy cards for a corporate and personal stylist. Must include logo,
Name: Belinda Forsey
Title: Director and Stylist
telephone : +61 8 8217 4592
email: belinda@thegarbledger.example
website: thegarbledger.example
Tag: Corporate Workwear & Uniform Specialist | Personal Stylist
Would like nice icons for telephone, email, website

Target Market(s)

Businesses wanting stylish uniforms, people wanting stylish wardrobes

Industry/Entity Type

Corporate Workwear Stylist

Contact Information for Business Card

I would like black, white and gold foiling incorporated in the design - possibly a touch of the other colours on my branding guide attached Name: Belinda Forsey Title: Director and Stylist telephone : +61 8 8217 4592 email: belinda@thegarbledger.example website: thegarbledger.example Tag: Corporate Workwear & Uniform Specialist | Personal Stylist Would like nice icons for telephone, email, website

Font styles to use
Other font styles liked:
• Raleway

Colors

Designer to choose colors to be used in the design.

Requirements
Must have
• Gold foil accents

```html
<!DOCTYPE html>
<html lang="en">
<head>
<meta charset="utf-8">
<title>The Garb Ledger – Business Cards</title>
<link rel="stylesheet" href="https://fonts.googleapis.com/css2?family=Dancing+Script:wght@500&family=Raleway:wght@500;600;700&display=swap">
<style>
  :root {
    --backdrop: #8f8f8f;
    --card-white: #e9e9eb;
    --card-black: #1f1f1f;
    --ink: #1c1c1c;
    --gold: #c9a63a;
  }
  * { margin: 0; padding: 0; box-sizing: border-box; }
  html, body {
    width: 1200px; height: 781px; overflow: hidden;
    background: var(--backdrop);
    font-family: "Raleway", sans-serif;
  }
  .canvas { position: relative; width: 1200px; height: 781px; }

  .card { position: absolute; width: 252px; height: 453px; }

  /* Front: contact side */
  .card--front {
    left: 278px; top: 100px;
    background: var(--card-white);
    border-top: 4px solid var(--gold);
  }
  .card--front .brand {
    position: absolute; right: 20px; top: 58px;
    font-size: 17px; font-weight: 700; color: var(--ink);
    letter-spacing: 0.5px;
  }
  .person { position: absolute; left: 24px; top: 258px; }
  .person__name {
    font-family: "Dancing Script", cursive;
    font-size: 25px; font-weight: 500; color: var(--gold);
    line-height: 1;
  }
  .person__title {
    margin-top: 8px; font-size: 13.5px; font-weight: 500; color: var(--ink);
  }
  .contacts {
    position: absolute; left: 22px; top: 350px; list-style: none;
  }
  .contacts li {
    display: flex; align-items: center; height: 19.5px;
    font-size: 12.5px; font-weight: 500; color: var(--ink);
  }
  .contacts li.contacts__web { font-weight: 700; letter-spacing: 0.4px; }
  .contacts svg {
    width: 13px; height: 13px; margin-right: 11px; flex: none;
    fill: none; stroke: var(--gold); stroke-width: 1.1;
  }

  /* Back: brand side */
  .card--back {
    left: 620px; top: 206px;
    background: var(--card-black);
  }
  .card--back .brand {
    position: absolute; left: 0; right: 0; top: 200px;
    text-align: center;
    font-size: 22px; font-weight: 700; color: var(--gold);
    letter-spacing: 1px;
  }
  .tagline {
    position: absolute; left: 0; right: 0; top: 371px;
    text-align: center; text-transform: uppercase;
    font-size: 10.5px; font-weight: 600; line-height: 15px;
    letter-spacing: 0.5px; color: var(--gold);
  }
</style>
</head>
<body>
<main class="canvas">

  <section class="card card--front">
    <div class="brand">The Garb Ledger</div>

    <div class="person">
      <p class="person__name">Belinda Forsey</p>
      <p class="person__title">Director and Stylist</p>
    </div>

    <ul class="contacts">
      <li>
        <svg viewBox="0 0 14 14"><path d="M3 1.5l2.2 2.6-1.3 1.5c.8 1.8 2.2 3.2 4 4l1.5-1.3 2.6 2.2-1.3 1.8C6.5 12 2 7.5 1.7 2.8z"/></svg>
        +61 8 8217 4592
      </li>
      <li>
        <svg viewBox="0 0 14 14"><rect x="1" y="3" width="12" height="8.5"/><path d="M1 3l6 5 6-5"/></svg>
        belinda@thegarbledger.example
      </li>
      <li class="contacts__web">
        <svg viewBox="0 0 14 14"><circle cx="7" cy="7" r="5.8"/><ellipse cx="7" cy="7" rx="2.5" ry="5.8"/><path d="M1.2 7h11.6"/></svg>
        thegarbledger.example
      </li>
    </ul>
  </section>

  <section class="card card--back">
    <div class="brand">The Garb Ledger</div>
    <p class="tagline">Corporate Workwear &amp;<br>Uniform Specialist<br>Personal Stylist</p>
  </section>

</main>
</body>
</html>
```